New Innovative Counselling and psychotherapy Service needs Business Card design

Keep it simple and professional. On one side, just company name and logo (perhaps in all blue) and maybe a tag line.

On other side (all white) my name and Qualifications in centre

Industry/Entity Type

Health And Wellness

Contact Information for Business Card

Derek Hollis
Counsellor & Psychotherapist
BSc (Psychol.), BA, Dip. (Couns. & Psych.), PG.Cert (CBT), MGVrA, NWTF

I will also require Mobile no, Email and web site address of which I'll pass on to final designer.

Font styles to use
Sans Serif

Requirements
Must have
• My Logo Only and please use the colours in logo that is in it.
Should not have
• Any other images

```html
<!DOCTYPE html>
<html lang="en">
<head>
<meta charset="utf-8">
<title>Harbor Lane – Business Card</title>
<link rel="stylesheet" href="https://fonts.googleapis.com/css2?family=Montserrat:wght@300;400;500&family=Nunito+Sans:wght@400;600&display=swap">
<style>
  :root {
    --page-bg: #e4e4e4;
    --card-white: #ffffff;
    --brand-blue: #45a6d9;
    --brand-green: #8cc152;
    --ink-dark: #4a4a4a;
    --ink-soft: #6d6d6d;
  }
  * { margin: 0; padding: 0; box-sizing: border-box; }
  html, body {
    width: 1200px;
    height: 900px;
    overflow: hidden;
    background: var(--page-bg);
  }
  .canvas {
    width: 1200px;
    height: 900px;
    display: flex;
    flex-direction: column;
    align-items: center;
    justify-content: center;
    gap: 60px;
  }
  .card {
    position: relative;
    width: 600px;
    height: 340px;
    overflow: hidden;
    box-shadow: 0 2px 6px rgba(0,0,0,0.12);
  }

  /* Front side */
  .card--front {
    background: var(--brand-blue);
    display: flex;
    align-items: center;
    justify-content: center;
  }
  .brand {
    display: flex;
    align-items: center;
    gap: 18px;
  }
  .brand__dot {
    width: 44px;
    height: 44px;
    border-radius: 50%;
    background: var(--card-white);
  }
  .brand__name {
    font-family: "Montserrat", sans-serif;
    font-weight: 300;
    font-size: 40px;
    letter-spacing: 0.5px;
    color: var(--card-white);
  }

  /* Back side */
  .card--back { background: var(--card-white); }
  .back__accent {
    position: absolute;
    right: 0;
    top: 0;
    width: 230px;
    height: 340px;
  }
  .details {
    position: absolute;
    left: 52px;
    top: 62px;
    font-family: "Nunito Sans", sans-serif;
  }
  .details__name {
    font-family: "Montserrat", sans-serif;
    font-weight: 400;
    font-size: 26px;
    color: var(--ink-dark);
    line-height: 1.1;
  }
  .details__role {
    font-size: 15px;
    font-weight: 600;
    color: var(--brand-blue);
    margin-top: 4px;
  }
  .qualifications {
    list-style: none;
    margin-top: 10px;
    font-size: 12px;
    line-height: 1.3;
    color: var(--ink-soft);
  }
  .contact {
    list-style: none;
    margin-top: 20px;
  }
  .contact__item {
    display: flex;
    align-items: center;
    gap: 10px;
    font-size: 15px;
    color: var(--ink-dark);
    margin-bottom: 6px;
  }
  .contact__icon {
    width: 18px;
    height: 18px;
    flex: none;
  }
</style>
</head>
<body>
<main class="canvas">

  <section class="card card--front" aria-label="Card front">
    <div class="brand">
      <span class="brand__dot"></span>
      <span class="brand__name">Harbor Lane</span>
    </div>
  </section>

  <section class="card card--back" aria-label="Card back">
    <svg class="back__accent" viewBox="0 0 230 340" aria-hidden="true">
      <circle cx="230" cy="170" r="150" fill="var(--brand-blue)"/>
    </svg>

    <div class="details">
      <h1 class="details__name">Derek Hollis</h1>
      <p class="details__role">Counsellor &amp; Psychotherapist</p>
      <ul class="qualifications">
        <li>BSc (Psychol.)</li>
        <li>BA, Dip. (Couns. &amp; Psych.)</li>
        <li>PG.Cert (CBT)</li>
        <li>MGVrA</li>
        <li>NWTF</li>
      </ul>
      <ul class="contact">
        <li class="contact__item">
          <svg class="contact__icon" viewBox="0 0 18 18" aria-hidden="true">
            <circle cx="9" cy="9" r="9" fill="var(--brand-green)"/>
            <path d="M6.2 4.8l1.4 1.8-.8 1.1c.5 1.1 1.4 2 2.5 2.5l1.1-.8 1.8 1.4-.7 1.5c-3.2-.2-6.3-3.3-6.5-6.5z" fill="#fff"/>
          </svg>
          <span>555 018 2741</span>
        </li>
        <li class="contact__item">
          <svg class="contact__icon" viewBox="0 0 18 18" aria-hidden="true">
            <circle cx="9" cy="9" r="9" fill="var(--brand-green)"/>
            <rect x="4.5" y="6" width="9" height="6.5" rx="1" fill="#fff"/>
            <path d="M4.8 6.4L9 9.6l4.2-3.2" fill="none" stroke="var(--brand-green)" stroke-width="1"/>
          </svg>
          <span>dhollis@mailbox.com</span>
        </li>
        <li class="contact__item">
          <svg class="contact__icon" viewBox="0 0 18 18" aria-hidden="true">
            <circle cx="9" cy="9" r="9" fill="var(--brand-green)"/>
            <g fill="none" stroke="#fff" stroke-width="1">
              <circle cx="9" cy="9" r="4.5"/>
              <ellipse cx="9" cy="9" rx="2" ry="4.5"/>
              <path d="M4.5 9h9"/>
            </g>
          </svg>
          <span>www.dhollispsy.com</span>
        </li>
      </ul>
    </div>
  </section>

</main>
</body>
</html>
```